"Vantarel Inc." Needs a Logo Design and Business Card

The name of the company is "Vantarel Inc."
Our Business decription, which should appear on the front of the Business Card along with the logo and business name is:
"Boutique Global Procurement and Management Services"
We offer the following SERVICES that should be listed on the back of the Business Card :
"Consultants"
"Management"
"Business Research & Development"
"Sourcing Agent"
"Distributors"
We would like to see designs that use the colors
burnt orange and,
stainless steel
Business card designs should be innovatively modern and contemporary
Telephone number and email address should be on the back of the card
Updates
The name of the firm is "Vantarel Inc.
Industry/Entity Type
Steel
Look and feel
Each slider illustrates characteristics of the customer's brand and the style your logo design should communicate.

```html
<!DOCTYPE html>
<html lang="en">
<head>
<meta charset="utf-8">
<title>Vantarel Inc. — Business Card Back</title>
<link rel="stylesheet" href="https://fonts.googleapis.com/css2?family=Poiret+One&display=swap">
<style>
  :root {
    --card-bg: #363636;
    --circle-large: #292929;
    --circle-small: rgba(255, 255, 255, 0.09);
    --band-bg: #282828;
    --steel: #b4b4b4;
    --burnt-orange: #f2643a;
  }
  * { margin: 0; padding: 0; box-sizing: border-box; }
  html, body {
    width: 720px;
    height: 1200px;
    overflow: hidden;
    background: var(--card-bg);
  }
  .card {
    position: relative;
    width: 720px;
    height: 1200px;
    background: var(--card-bg);
    font-family: "Poiret One", sans-serif;
    overflow: hidden;
  }
  .backdrop {
    position: absolute;
    inset: 0;
  }
  .brand-name {
    position: absolute;
    right: 83px;
    top: 242px;
    font-size: 56px;
    line-height: 1;
    color: var(--steel);
    white-space: nowrap;
  }
  .services {
    list-style: none;
    position: absolute;
    right: 87px;
    top: 332px;
    text-align: right;
    color: var(--burnt-orange);
    font-size: 43px;
    line-height: 46px;
  }
  .services li { margin-bottom: 42px; white-space: nowrap; }
  .services li.two-line { margin-bottom: 42px; }
  .contact-band {
    position: absolute;
    left: 0;
    top: 984px;
    width: 720px;
    height: 93px;
    background: var(--band-bg);
    text-align: center;
    color: var(--burnt-orange);
  }
  .contact-phone {
    display: block;
    margin-top: 10px;
    font-size: 31px;
    line-height: 38px;
    letter-spacing: 4px;
  }
  .contact-email {
    display: block;
    font-size: 33px;
    line-height: 40px;
    letter-spacing: 3px;
  }
</style>
</head>
<body>
  <main class="card">
    <svg class="backdrop" width="720" height="1200" viewBox="0 0 720 1200" aria-hidden="true">
      <circle class="circle-large" cx="342" cy="348" r="243" fill="var(--circle-large)"/>
      <circle class="circle-small" cx="174" cy="600" r="141" fill="var(--circle-small)"/>
    </svg>

    <h1 class="brand-name">VANTAREL Inc.</h1>

    <ul class="services">
      <li>Consultants</li>
      <li>Management</li>
      <li class="two-line">Research<br>&amp; Development</li>
      <li>Sourcing Agents</li>
      <li>Distributors</li>
    </ul>

    <footer class="contact-band">
      <span class="contact-phone">1-888-555-0142</span>
      <span class="contact-email">contact-us@vantarelintl.com</span>
    </footer>
  </main>
</body>
</html>
```